Design some Business Cards

Create a set of business cards for circle of Venmora.
The cards should be somehow indicative of the level/ status age group of the members, which i why a small description of the stages is included.
The card should look professional and colours and designs should match or complement the initial scheme.

```html
<!DOCTYPE html>
<html lang="en">
<head>
<meta charset="utf-8">
<title>circle of Venmora — Business Cards</title>
<link rel="stylesheet" href="https://fonts.googleapis.com/css2?family=Raleway:wght@400;500;600&display=swap">
<style>
  :root {
    --green: #6b9a4f;
    --green-deep: #557f3c;
    --photo-light: #eef3ea;
    --photo-mid: #d9e5d2;
    --paper: #ffffff;
    --ink: #3a3a3a;
    --canvas: #ecedeb;
  }
  html, body {
    margin: 0;
    padding: 0;
    width: 1200px;
    height: 749px;
    overflow: hidden;
    background: var(--canvas);
  }
  .sheet {
    position: relative;
    width: 1200px;
    height: 749px;
    font-family: "Raleway", sans-serif;
  }
  .card {
    position: absolute;
    top: 220px;
    width: 540px;
    height: 310px;
    box-shadow: 0 10px 28px rgba(0,0,0,0.18);
    background: var(--paper);
  }
  .card--front { left: 40px; }
  .card--back { left: 620px; }
  .card svg { display: block; width: 540px; height: 310px; }
  .org-name { font-size: 19px; font-weight: 500; fill: var(--ink); }
  .brand { font-size: 44px; font-weight: 500; fill: var(--green); }
  .brand--back { font-size: 40px; }
  .website { font-size: 12px; font-weight: 500; fill: var(--green); }
  .detail { font-size: 14px; font-weight: 500; fill: var(--ink); }
  .detail--light { fill: #ffffff; font-size: 13px; }
  .icon-ring { fill: none; stroke: #ffffff; stroke-width: 1.6; }
  .icon-ring--green { stroke: var(--green); }
  .icon-line { fill: none; stroke: #ffffff; stroke-width: 1.6; stroke-linecap: round; stroke-linejoin: round; }
  .icon-line--green { stroke: var(--green); }
</style>
</head>
<body>
<main class="sheet">

  <section class="card card--front" aria-label="Business card front">
    <svg viewBox="0 0 540 310" xmlns="http://www.w3.org/2000/svg">
      <defs>
        <linearGradient id="photoTone" x1="0" y1="0" x2="1" y2="1">
          <stop offset="0" stop-color="var(--photo-mid)"/>
          <stop offset="0.55" stop-color="var(--photo-light)"/>
          <stop offset="1" stop-color="var(--photo-mid)"/>
        </linearGradient>
      </defs>

      <rect class="photo-field" width="540" height="310" fill="url(#photoTone)" role="img" aria-label="Soft photograph of a scientist working at a laboratory microscope"/>

      <polygon class="top-band" points="0,0 540,0 540,36 300,78 0,34" fill="var(--paper)"/>
      <polyline points="0,34 300,78 540,36" fill="none" stroke="var(--green)" stroke-width="2"/>
      <text class="org-name" x="395" y="44" text-anchor="middle">circle of Venmora</text>

      <circle cx="178" cy="150" r="6" fill="var(--green)"/>
      <text class="brand" x="192" y="165">Venmora</text>

      <polygon class="panel-phone" points="0,108 140,150 205,232 0,262" fill="var(--green)"/>
      <g class="icon-phone" transform="translate(62,188)">
        <circle class="icon-ring" r="13"/>
        <rect class="icon-line" x="-5" y="-8" width="10" height="16" rx="2"/>
        <line class="icon-line" x1="-2" y1="5" x2="2" y2="5"/>
      </g>
      <text class="detail detail--light" x="14" y="228">(+00) 00.000.000</text>

      <polygon class="bottom-band" points="0,262 205,232 300,248 300,310 0,310" fill="var(--paper)"/>
      <polyline points="0,262 205,232 300,248" fill="none" stroke="var(--green)" stroke-width="2"/>
      <g class="icon-person" transform="translate(208,256)">
        <circle class="icon-ring icon-ring--green" r="12"/>
        <circle class="icon-line icon-line--green" cy="-3" r="3.5"/>
        <path class="icon-line icon-line--green" d="M-6,7 Q0,-1 6,7"/>
      </g>
      <text class="detail" x="208" y="284" text-anchor="middle">your name</text>
      <text class="detail" x="208" y="300" text-anchor="middle">your job</text>

      <polygon class="panel-email" points="300,248 420,212 540,236 540,310 300,310" fill="var(--green)"/>
      <g class="icon-at" transform="translate(430,254)">
        <circle class="icon-ring" r="13"/>
        <text x="0" y="5" text-anchor="middle" fill="#ffffff" font-size="14" font-weight="600">@</text>
      </g>
      <text class="detail detail--light" x="430" y="290" text-anchor="middle">yourmail@venmora.org</text>
    </svg>
  </section>

  <section class="card card--back" aria-label="Business card back">
    <svg viewBox="0 0 540 310" xmlns="http://www.w3.org/2000/svg">
      <rect width="540" height="310" fill="var(--paper)"/>

      <circle cx="170" cy="115" r="6" fill="var(--green)"/>
      <text class="brand brand--back" x="184" y="130">Venmora</text>
      <text class="website" x="268" y="150" text-anchor="middle">yourwebsite.com</text>

      <polygon class="panel-left" points="0,150 175,222 0,268" fill="var(--green)"/>

      <polygon class="address-band" points="0,268 175,222 400,222 400,310 0,310" fill="var(--paper)"/>
      <polyline points="0,268 175,222 400,222" fill="none" stroke="var(--green)" stroke-width="2"/>
      <g class="icon-pin" transform="translate(265,240)">
        <circle class="icon-ring icon-ring--green" r="12"/>
        <path class="icon-line icon-line--green" d="M0,7 C-5,1 -5,-2 -5,-3 A5,5 0 0 1 5,-3 C5,-2 5,1 0,7 Z"/>
      </g>
      <text class="detail" x="265" y="272" text-anchor="middle">00 Street address</text>
      <text class="detail" x="265" y="290" text-anchor="middle">city code, city, country</text>

      <polygon class="panel-right" points="400,222 540,188 540,310 400,310" fill="var(--green)"/>
    </svg>
  </section>

</main>
</body>
</html>
```